Promotional poster for a vintage motorcycle show.

Vertically oriented, based on 11 x 17 inch proportions

Though not to the exclusion of other design concepts, stylistically perhaps something evoking a vintage (early-mid 20th century) 2-3 color silk screen style event poster.

In addition to some sort of eyecatching, vintage / antique motorbike oriented graphic (preferably not Brennick Vasquel based), the poster should include the following text and info:

3rd Annual Morven Tolliash Vintage Motorcycle Show
Bordentown City, N.J.
October 1st (rain date Oct. 2nd)
11am-4pm

Presented in conjunction with the 27th Annual Lanternfall Festival

For further info, or to register your pre-1992 bike contact:
Oswin@gearpatina.example or 555-214-9083

Sponsored by:
UpperMarshwickQuarterGuild.example
Gearpatina.example

Promotional

Must have
• See above project description
Nice to have
• See above project describtion

```html
<!DOCTYPE html>
<html lang="en">
<head>
<meta charset="utf-8">
<title>Morven Tolliash Vintage Motorcycle Show</title>
<link rel="stylesheet" href="https://fonts.googleapis.com/css2?family=Titan+One&family=Bangers&display=swap">
<style>
  :root {
    --poster-red: #ff1a0d;
    --ink: #0a0a0a;
    --paper: #ffffff;
  }
  html, body {
    margin: 0;
    padding: 0;
    width: 777px;
    height: 1200px;
    overflow: hidden;
    background: var(--poster-red);
  }
  .poster {
    position: relative;
    width: 777px;
    height: 1200px;
    background: var(--poster-red);
    overflow: hidden;
    font-family: "Titan One", sans-serif;
    color: var(--ink);
  }
  .edition-badge {
    position: absolute;
    left: 50px; top: 22px;
    width: 120px; height: 120px;
    border-radius: 50%;
    background: var(--paper);
    display: flex;
    flex-direction: column;
    align-items: center;
    justify-content: center;
    transform: rotate(-8deg);
    font-family: "Bangers", sans-serif;
    line-height: 0.9;
  }
  .edition-badge .ordinal { font-size: 44px; }
  .edition-badge .ordinal sup { font-size: 22px; }
  .edition-badge .label { font-size: 28px; }
  .show-name {
    position: absolute;
    left: 186px; top: 46px;
    width: 560px;
    text-align: center;
    margin: 0;
    font-size: 50px;
    font-weight: 400;
    letter-spacing: 1px;
    text-shadow: -3px 3px 0 var(--paper), -5px 5px 0 var(--ink);
    white-space: nowrap;
  }
  .headline-art {
    position: absolute;
    left: 0; top: 0;
    width: 777px; height: 500px;
  }
  .headline-word {
    font-family: "Bangers", sans-serif;
    fill: var(--paper);
    stroke: var(--ink);
    stroke-width: 2;
    paint-order: stroke;
    filter: drop-shadow(5px 5px 0 var(--ink));
  }
  .show-oval {
    position: absolute;
    left: 502px; top: 330px;
    width: 218px; height: 124px;
    border-radius: 50%;
    background: var(--paper);
    display: flex;
    align-items: center;
    justify-content: center;
    font-size: 52px;
    text-shadow: -2px 2px 0 var(--poster-red);
  }
  .rider-art {
    position: absolute;
    left: 0; top: 0;
    width: 777px; height: 760px;
  }
  .location {
    position: absolute;
    left: 0; top: 752px;
    width: 777px;
    text-align: center;
    margin: 0;
    font-size: 56px;
    font-weight: 400;
    letter-spacing: 1px;
  }
  .schedule {
    position: absolute;
    left: 0; top: 820px;
    width: 777px;
    text-align: center;
    margin: 0;
    font-size: 24px;
  }
  .festival-panel {
    position: absolute;
    left: 32px; top: 860px;
    width: 706px; height: 176px;
    background: var(--paper);
    text-align: center;
    font-family: "Bangers", sans-serif;
    letter-spacing: 1px;
  }
  .festival-panel p { margin: 0; line-height: 1; }
  .festival-panel .intro { font-size: 34px; margin-top: 14px; }
  .festival-panel .edition { font-size: 40px; margin-top: 6px; }
  .festival-panel .festival { font-size: 62px; margin-top: 4px; }
  .contact {
    position: absolute;
    left: 0; top: 1046px;
    width: 777px;
    text-align: center;
    color: var(--paper);
    font-family: "Bangers", sans-serif;
    letter-spacing: 1px;
  }
  .contact p { margin: 0; line-height: 1.18; font-size: 23px; }
  .contact .sponsor-label { font-size: 17px; margin-top: 4px; }
  .contact .sponsors { font-size: 27px; margin-top: 4px; }
</style>
</head>
<body>
  <main class="poster">
    <div class="edition-badge">
      <span class="ordinal">3<sup>RD</sup></span>
      <span class="label">ANNUAL</span>
    </div>
    <h1 class="show-name">MORVEN TOLLIASH</h1>

    <svg class="rider-art" viewBox="0 0 777 760" role="img" aria-label="Illustration of a racer crouched low over a vintage café racer motorcycle with race number 3, speed lines behind">
      <defs>
        <radialGradient id="riderTone" cx="55%" cy="60%" r="60%">
          <stop offset="0%" stop-color="#2c2c2c"/>
          <stop offset="100%" stop-color="#0c0c0c"/>
        </radialGradient>
      </defs>
      <path fill="url(#riderTone)" d="M90,610 Q96,530 190,500 L290,494 L400,436 Q440,404 486,420 L560,478 L690,488 Q734,560 730,640 Q722,740 600,740 L130,740 Q90,722 90,610 Z"/>
    </svg>

    <svg class="headline-art" viewBox="0 0 777 500" aria-label="Vintage Motorcycle">
      <text class="headline-word" x="72" y="352" font-size="240" textLength="98" lengthAdjust="spacingAndGlyphs">V</text>
      <text class="headline-word" x="170" y="252" font-size="116" textLength="320" lengthAdjust="spacingAndGlyphs" transform="rotate(-8 170 252)">INTAGE</text>
      <text class="headline-word" x="158" y="484" font-size="240" textLength="114" lengthAdjust="spacingAndGlyphs">M</text>
      <text class="headline-word" x="276" y="388" font-size="124" textLength="412" lengthAdjust="spacingAndGlyphs" transform="rotate(-10 276 388)">OTORCYCLE</text>
    </svg>

    <div class="show-oval">SHOW</div>

    <h3 class="location">BORDENTOWN CITY, NJ</h3>
    <p class="schedule">OCTOBER 1ST (RAIN DATE OCT 2ND)•11AM -4PM</p>
    <section class="festival-panel">
      <p class="intro">PRESENTED IN CONJUCTION WITH THE</p>
      <p class="edition">27TH ANNUAL</p>
      <p class="festival">LANTERNFALL FESTIVAL</p>
    </section>
    <footer class="contact">
      <p>FOR FURTHER INFO OR TO REGISTER YOUR PRE-1992 BIKE CONTACT:</p>
      <p>OSWIN@GEARPATINA.EXAMPLE OR 555-214-9083</p>
      <p>VENDORS INQUIRIES WELCOMED</p>
      <p class="sponsor-label">SPONSORED BY:</p>
      <p class="sponsors">UpperMarshwickQuarterGuild.example &amp; Gearpatina.example</p>
    </footer>
  </main>
</body>
</html>
```